Velmora - 3D medical animations and high end visual content

Our company creates high end visual content and animations for medical global companies.
Our website - www.velmora-studio.example
We would like to have an amazing business card for our CEO that he can use in the following exhebitions he is going to attend.
It is very important that the design will be memorable and diffrent. It has to reflect our brand design (you can have it from our website)
We would like to transmit innovation, prestige, luxury, aesthetics.
The card has to be Double Sided

Target Market(s)

Marketing managers in medical global companys

Industry/Entity Type

It Company

Contact Information for Business Card

Requirements
Nice to have
• It is very important that the design will be memorable and diffrent. It has to reflect our brand design (you can have it from our website)

```html
<!DOCTYPE html>
<html lang="en">
<head>
<meta charset="utf-8">
<title>Velmora – Business Card</title>
<link rel="stylesheet" href="https://fonts.googleapis.com/css2?family=Montserrat:wght@400;500;600;700&display=swap">
<style>
  :root {
    --stage: #3a3a3c;
    --stage-edge: #2a2a2b;
    --card-black: #050608;
    --ink-white: #f4f6f8;
    --ink-grey: #a9b0b8;
    --accent-blue: #3aa0e8;
    --deep-blue: #0b2c56;
    --glow-blue: #4fb6ff;
    --warm: #c8642a;
  }
  * { box-sizing: border-box; margin: 0; padding: 0; }
  html, body { width: 900px; height: 1200px; overflow: hidden; }
  body {
    background: radial-gradient(ellipse at 50% 45%, var(--stage) 0%, var(--stage-edge) 100%);
    font-family: "Montserrat", Arial, sans-serif;
    position: relative;
  }
  .card {
    position: absolute;
    left: 70px;
    width: 760px;
    height: 434px;
    overflow: hidden;
    background: var(--card-black);
    box-shadow: 0 14px 30px rgba(0,0,0,.55);
  }
  .card--front { top: 150px; }
  .card--back { top: 640px; }

  .front__visual {
    position: absolute;
    right: 0; top: 0;
    width: 64%; height: 100%;
    background:
      radial-gradient(ellipse 40% 38% at 55% 38%, rgba(79,182,255,.75) 0%, rgba(30,110,200,.35) 45%, rgba(0,0,0,0) 75%),
      radial-gradient(ellipse 30% 28% at 78% 70%, rgba(60,150,230,.45) 0%, rgba(0,0,0,0) 70%),
      linear-gradient(90deg, var(--card-black) 0%, #061426 35%, #0a2546 70%, #071a33 100%);
  }
  .brand {
    position: absolute;
    left: 44px; top: 92px;
    width: 300px;
  }
  .brand__name {
    color: var(--ink-white);
    font-weight: 500;
    font-size: 44px;
    letter-spacing: 2px;
    line-height: 1;
  }
  .brand__rule {
    margin-top: 10px;
    height: 1px;
    width: 238px;
    background: var(--ink-grey);
  }
  .person {
    position: absolute;
    left: 44px; top: 248px;
  }
  .person__name {
    color: var(--ink-white);
    font-weight: 600;
    font-size: 17px;
    letter-spacing: .5px;
  }
  .person__role {
    color: var(--warm);
    font-size: 11px;
    margin-top: 3px;
  }
  .contact {
    position: absolute;
    left: 44px; top: 310px;
    list-style: none;
  }
  .contact__item {
    display: flex;
    align-items: center;
    gap: 8px;
    color: var(--ink-white);
    font-size: 12px;
    height: 21px;
  }
  .contact__icon { width: 12px; height: 12px; flex: none; }

  .back__visual {
    position: absolute; inset: 0;
    background:
      radial-gradient(ellipse 18% 30% at 22% 68%, rgba(200,100,42,.85) 0%, rgba(120,50,20,.4) 55%, rgba(0,0,0,0) 80%),
      radial-gradient(ellipse 45% 40% at 65% 70%, rgba(170,200,220,.35) 0%, rgba(0,0,0,0) 70%),
      radial-gradient(ellipse 60% 50% at 70% 25%, rgba(40,110,170,.5) 0%, rgba(0,0,0,0) 75%),
      linear-gradient(135deg, #0c1c2a 0%, #18354a 45%, #0a1520 100%);
  }
  .back__brand {
    position: absolute;
    left: 420px; top: 112px;
    width: 260px;
  }
  .back__brand .brand__rule { width: 238px; }
</style>
</head>
<body>
  <section class="card card--front">
    <div class="front__visual" role="img" aria-label="Glowing blue particle cloud forming an abstract molecular structure"></div>
    <div class="brand">
      <div class="brand__name">VELMORA</div>
      <div class="brand__rule"></div>
    </div>
    <div class="person">
      <div class="person__name">NOAM KELLER</div>
      <div class="person__role">Founder &amp; CEO</div>
    </div>
    <ul class="contact">
      <li class="contact__item">
        <svg class="contact__icon" viewBox="0 0 12 12"><path d="M3 1l2 2-1 1.5c.6 1.3 1.6 2.3 2.9 2.9L8.4 6.4l2 2L9 10.5C5 10.2 1.8 7 1.5 3z" fill="var(--accent-blue)"/></svg>
        +000-52-4410387
      </li>
      <li class="contact__item">
        <svg class="contact__icon" viewBox="0 0 12 12"><path d="M3 1l2 2-1 1.5c.6 1.3 1.6 2.3 2.9 2.9L8.4 6.4l2 2L9 10.5C5 10.2 1.8 7 1.5 3z" fill="var(--accent-blue)"/></svg>
        +000-77-3185204
      </li>
      <li class="contact__item">
        <svg class="contact__icon" viewBox="0 0 12 12"><rect x="1" y="2.5" width="10" height="7" rx="1" fill="var(--accent-blue)"/><path d="M1.5 3l4.5 3.5L10.5 3" stroke="var(--card-black)" fill="none"/></svg>
        noam@velmora-studio.example
      </li>
      <li class="contact__item">
        <svg class="contact__icon" viewBox="0 0 12 12"><circle cx="6" cy="6" r="5" fill="none" stroke="var(--accent-blue)" stroke-width="1.2"/><path d="M1 6h10M6 1c-2.5 3-2.5 7 0 10M6 1c2.5 3 2.5 7 0 10" stroke="var(--accent-blue)" fill="none"/></svg>
        www.velmora-studio.example
      </li>
    </ul>
  </section>

  <section class="card card--back">
    <div class="back__visual" role="img" aria-label="Robotic hand with a glowing orange core reaching toward a human hand in a dark blue tech space"></div>
    <div class="brand back__brand">
      <div class="brand__name">VELMORA</div>
      <div class="brand__rule"></div>
    </div>
  </section>
</body>
</html>
```